DM - management consultant

Business card - contemporary design

Front info
Dorian Maples

(Address not necessary)
PO Box 7386
Belmont, CA 94002

(650) 555-0143
dm@dorianmapl.es

Chirper: dmq527
Facenook: /Dorian.Maples
Linkwell: /in/dorianmaples

Back or Front
www.dorianmaples.net
Facilitation & coaching, change management, strategic partnerships, business improvement

Target Market(s)

High tech businesses - mostly startups in Silicon Valley

Industry/Entity Type

Business

Font styles to use
Sans Serif

Colors

Designer to choose colors to be used in the design.

```html
<!DOCTYPE html>
<html lang="en">
<head>
<meta charset="utf-8">
<title>Dorian Maples – Business Card</title>
<link rel="stylesheet" href="https://fonts.googleapis.com/css2?family=Roboto:wght@400;500;700&display=swap">
<style>
  :root {
    --bg: #d9d4cd;
    --ink: #1c1c1c;
    --black: #0d0d0d;
    --red: #c8171d;
    --white: #ffffff;
    --ghost: #ececec;
  }
  * { margin: 0; padding: 0; box-sizing: border-box; }
  html, body {
    width: 1200px; height: 784px; overflow: hidden;
    background: var(--bg);
    font-family: "Roboto", Arial, sans-serif;
  }
  .canvas {
    position: relative; width: 1200px; height: 784px;
    display: flex; align-items: center; justify-content: center; gap: 40px;
  }
  .card {
    position: relative; width: 540px; height: 309px; overflow: hidden;
    box-shadow: 0 10px 24px rgba(0,0,0,.25);
  }

  /* back side */
  .card-back {
    background: radial-gradient(ellipse at 50% 35%, #2a2a2a 0%, var(--black) 75%);
    text-align: center; color: var(--white);
  }
  .back-initials {
    margin-top: 40px;
    font-weight: 700; font-size: 44px; line-height: 1;
    color: var(--red);
  }
  .back-url {
    margin-top: 12px;
    font-size: 14px; letter-spacing: 4px; color: var(--red); font-weight: 500;
  }
  .services { list-style: none; margin-top: 20px; }
  .services li {
    font-size: 15px; font-variant: small-caps; letter-spacing: 3px;
    line-height: 27px; font-weight: 500;
  }

  /* front side */
  .card-front { background: var(--white); color: var(--ink); }
  .front-initials {
    position: absolute; left: 28px; top: 70px;
    font-weight: 700; font-size: 56px; line-height: 1;
    color: var(--red);
  }
  .ghost-initials {
    position: absolute; right: -10px; top: 104px;
    font-weight: 700; font-size: 130px; line-height: 1;
    color: var(--ghost);
  }
  .identity { position: absolute; left: 150px; top: 56px; }
  .name { font-weight: 700; font-size: 27px; line-height: 1; }
  .rule { width: 318px; height: 2px; background: var(--red); margin: 7px 0 6px -4px; }
  .title { font-size: 10px; letter-spacing: 5px; font-weight: 500; text-transform: uppercase; }

  .contacts { position: absolute; left: 30px; top: 158px; list-style: none; }
  .contacts li {
    display: flex; align-items: center; gap: 6px;
    font-size: 14px; line-height: 18px;
  }
  .contacts li.gap { margin-top: 8px; }
  .contacts svg { width: 11px; height: 11px; flex: none; }
  .square { width: 11px; height: 11px; background: var(--red); flex: none; }

  .base-band { position: absolute; left: 0; bottom: 0; width: 540px; height: 60px; }
</style>
</head>
<body>
<main class="canvas">

  <section class="card card-back" aria-label="Card back">
    <div class="back-initials">DM</div>
    <p class="back-url">www.dorianmaples.net</p>
    <ul class="services">
      <li>Facilitation &amp; Coaching</li>
      <li>Change Management</li>
      <li>Strategic Partnerships</li>
      <li>Business Improvement</li>
    </ul>
  </section>

  <section class="card card-front" aria-label="Card front">
    <div class="ghost-initials" aria-hidden="true">DM</div>
    <div class="front-initials">DM</div>
    <div class="identity">
      <h1 class="name">Dorian Maples</h1>
      <div class="rule"></div>
      <p class="title">Management Consultant</p>
    </div>

    <ul class="contacts">
      <li>
        <svg viewBox="0 0 12 12" aria-hidden="true"><path fill="#c8171d" d="M2.4 0.6l2 2-1 1.4c.6 1.4 1.8 2.6 3.2 3.2l1.4-1 2 2-1.4 1.8C4.8 9.4 1.4 6 .6 2z"/></svg>
        (650) 555-0143
      </li>
      <li>
        <svg viewBox="0 0 12 12" aria-hidden="true"><rect x="0.5" y="2" width="11" height="8" fill="#c8171d"/><path d="M0.8 2.4L6 6.6l5.2-4.2" stroke="#fff" stroke-width="1" fill="none"/></svg>
        dm@dorianmapl.es
      </li>
      <li class="gap"><span class="square"></span>Chirper: dmq527</li>
      <li><span class="square"></span>Facenook: /Dorian.Maples</li>
      <li><span class="square"></span>Linkwell: /in/dorianmaples</li>
    </ul>

    <svg class="base-band" viewBox="0 0 540 60" aria-hidden="true">
      <polygon points="0,36 540,12 540,15 0,39" fill="#c8171d"/>
      <polygon points="0,43 540,19 540,60 0,60" fill="#0d0d0d"/>
    </svg>
  </section>

</main>
</body>
</html>
```